Environmental Plastics Infographic on Marine Debris

We need a series of infographics that can be used individually or as a combined presentation. We'd like the combined piece to include an introduction and conclusion along with 4-5 infographics. Each infographic (information unit) should also work as a standalone. We are trying to help people visualize size proportions and ratios to put the plastics marine debris problem in perspective. Our key point is concerning polystyrene foam which represents 35 tons. We are looking for something creative to help people understand what the problem represents in terms they are familiar with.

To view our typical company design/style please see our website at www.harbenfoamworks.org. Our primary RGB colors are: (187,140,9); (94,47,29); (94,138,164); and (164,167,15). Secondary RGB colors are (249,162,28) and (218,210,208). Our title/header font is DIN Next LT Pro and our copy font is Calibri 10.5 pt. We can deviate from the font specification if beneficial and welcome interesting text treatments and typography.

Need extra days to review

Target Market(s)

international brand manufacturers (brenloch, tavix), US legislators & government agencies

Font styles to use
Sans Serif

Requirements
Must have
• Sufficient white space. Easy to grasp message concept with visual components.

```html
<!DOCTYPE html>
<html lang="en">
<head>
<meta charset="utf-8">
<title>How Will Polystyrene Bans Improve Ocean Health?</title>
<link href="https://fonts.googleapis.com/css2?family=Roboto+Condensed:wght@700&family=Roboto:wght@300;400;700&display=swap" rel="stylesheet">
<style>
  :root {
    --steel: #5e8aa4;
    --steel-light: #cdd8e2;
    --mist: #dde4ea;
    --olive: #a4a73a;
    --orange: #f9a21c;
    --crimson: #d81b5c;
    --ink: #4a4a4a;
    --map-grey: #eceeef;
    --map-land: #5f6062;
    --paper: #ffffff;
  }
  * { margin: 0; padding: 0; box-sizing: border-box; }
  html, body { width: 848px; height: 1200px; overflow: hidden; background: var(--paper); }
  .canvas { position: relative; width: 848px; height: 1200px; font-family: "Roboto", Arial, sans-serif; color: var(--ink); }
  .headline {
    position: absolute; left: 66px; top: 78px;
    font-family: "Roboto Condensed", "Arial Narrow", sans-serif; font-weight: 700;
    font-size: 28px; line-height: 33px; color: var(--steel);
  }
  .section-title {
    position: absolute; left: 66px; top: 500px;
    font-family: "Roboto Condensed", "Arial Narrow", sans-serif; font-weight: 700;
    font-size: 28px; color: var(--steel);
  }
  .report-card { position: absolute; left: 40px; top: 180px; width: 230px; height: 260px; }
  .report-text {
    position: absolute; left: 70px; top: 241px; width: 170px;
    font-size: 13px; line-height: 16.5px; color: #fff; font-weight: 300;
  }
  .intro {
    position: absolute; left: 283px; top: 236px; width: 430px;
    font-size: 13px; line-height: 16.5px; font-weight: 300; color: var(--ink);
  }
  .intro p + p { margin-top: 16px; }
  .art { position: absolute; left: 0; top: 0; }
  .legend { position: absolute; left: 300px; top: 822px; list-style: none; }
  .legend li { display: flex; align-items: center; height: 35px; font-size: 14px; font-weight: 300; }
  .legend .swatch { width: 29px; height: 22px; margin-right: 20px; }
  .stats { position: absolute; left: 66px; top: 960px; list-style: none; }
  .stat { display: flex; align-items: center; height: 60px; }
  .stat-figure {
    width: 104px; font-family: "Roboto Condensed", "Arial Narrow", sans-serif;
    font-weight: 700; font-size: 50px; letter-spacing: -1px;
  }
  .stat-text { font-size: 13px; line-height: 16px; font-weight: 300; width: 220px; }
  .minor { color: var(--crimson); }
  .map { position: absolute; left: 525px; top: 872px; width: 258px; height: 243px; background: linear-gradient(135deg, var(--map-land) 0 30%, var(--map-grey) 30% 70%, var(--map-land) 70%); }
</style>
</head>
<body>
<div class="canvas">
  <h1 class="headline">How Will Polystyrene Bans<br>Improve Ocean Health?</h1>

  <svg class="art" width="848" height="1200" viewBox="0 0 848 1200" aria-hidden="true">
    <!-- banned foam sign -->
    <text x="540" y="195" font-family="Roboto Condensed, sans-serif" font-weight="700" font-size="78" fill="var(--steel-light)">?</text>
    <text x="585" y="238" font-family="Roboto Condensed, sans-serif" font-weight="700" font-size="100" fill="var(--mist)">?</text>
    <circle cx="681" cy="110" r="68" fill="#ededeb"/>
    <text x="696" y="160" font-family="Roboto Condensed, sans-serif" font-weight="700" font-size="60" fill="var(--steel)">?</text>
    <circle cx="681" cy="110" r="75" fill="none" stroke="var(--steel)" stroke-width="16"/>
    <line x1="628" y1="57" x2="734" y2="163" stroke="var(--steel)" stroke-width="16"/>

    <!-- report card -->
    <rect x="48" y="195" width="186" height="240" fill="var(--mist)" transform="rotate(-3 141 315)"/>
    <rect x="58" y="192" width="186" height="236" fill="#c7d3dd"/>
    <path d="M62 190 H206 L246 230 V422 H62 Z" fill="var(--steel)"/>
    <path d="M206 190 V230 H246 Z" fill="#8fa9bd"/>
    <circle cx="85" cy="208" r="7" fill="none" stroke="#8fa9bd" stroke-width="2.5"/>
    <line x1="90" y1="213" x2="96" y2="219" stroke="#8fa9bd" stroke-width="2.5"/>
    <circle cx="96" cy="390" r="22" fill="#8fa9bd"/>
    <path d="M96 368 A22 22 0 0 1 96 412 Z" fill="#a9bccb"/>
    <rect x="126" y="373" width="28" height="5" fill="#a9bccb"/>
    <rect x="126" y="385" width="96" height="3" fill="#8fa9bd"/>
    <rect x="126" y="393" width="96" height="3" fill="#8fa9bd"/>
    <rect x="126" y="401" width="70" height="3" fill="#8fa9bd"/>

    <!-- pie chart -->
    <path d="M163 700 A108 108 0 0 1 150 915 L163 808 Z" fill="var(--orange)"/>
    <path d="M163 808 L150 915 A108 108 0 0 1 163 700 Z" fill="var(--olive)"/>
    <text x="70" y="832" font-family="Roboto Condensed, sans-serif" font-weight="700" font-size="40" fill="#fff">47<tspan font-size="26">%</tspan></text>
    <text x="176" y="840" font-family="Roboto Condensed, sans-serif" font-weight="700" font-size="40" fill="#fff">52<tspan font-size="26">%</tspan></text>

    <!-- zoom detail -->
    <line x1="120" y1="704" x2="302" y2="610" stroke="var(--steel)" stroke-width="3"/>
    <line x1="190" y1="772" x2="330" y2="790" stroke="var(--steel)" stroke-width="3"/>
    <path d="M430 558 A124 124 0 0 1 430 806 Z" fill="var(--orange)"/>
    <path d="M430 558 A124 124 0 0 0 430 806 Z" fill="var(--olive)"/>
    <line x1="430" y1="558" x2="429" y2="806" stroke="var(--crimson)" stroke-width="3"/>
    <circle cx="430" cy="682" r="136" fill="none" stroke="var(--steel)" stroke-width="3"/>
    <circle cx="163" cy="722" r="46" fill="none" stroke="var(--steel)" stroke-width="12"/>
    <line x1="202" y1="750" x2="282" y2="772" stroke="var(--steel)" stroke-width="16"/>

    <!-- poster -->
    <circle cx="653" cy="820" r="8" fill="var(--steel)"/>
    <line x1="653" y1="820" x2="560" y2="850" stroke="var(--steel)" stroke-width="2.5"/>
    <line x1="653" y1="820" x2="746" y2="850" stroke="var(--steel)" stroke-width="2.5"/>
    <rect x="510" y="848" width="288" height="24" fill="var(--steel)"/>
    <rect x="510" y="1115" width="288" height="13" fill="var(--steel)"/>
  </svg>

  <div class="map" role="img" aria-label="Map of the North Pacific marking the garbage patch with a debris bag icon"></div>

  <p class="report-text">A recent report looks at the role plastics play in marine debris that sheds light on previous assumptions about how different plastics contribute to the problem and where its coming from.</p>

  <div class="intro">
    <p>In this ground breaking study, scientists conducted cutting-edge research at a much larger scale than had ever been done before. Over the course of three years, an international team including The Tidewater Recovery Trust, six universities, and an aerial sensor company, collected data and mapped debris fields for the Great Pacific Garbage Patch, one of the most problematic plastic pollution hot spots.</p>
    <p>Polystyrene ban legislation imply product restrictions will minimize plastic marine debris.</p>
  </div>

  <h2 class="section-title">Let’s take a closer look.</h2>

  <ul class="legend">
    <li><span class="swatch" style="background:var(--crimson)"></span>Foamed Plastics</li>
    <li><span class="swatch" style="background:var(--olive)"></span>Hard Plastics</li>
    <li><span class="swatch" style="background:var(--orange)"></span>Fishing Gear</li>
  </ul>

  <ul class="stats">
    <li class="stat"><span class="stat-figure" style="color:var(--orange)">52%</span><span class="stat-text">is mostly abandoned fishing gear, not consumer plastics.</span></li>
    <li class="stat"><span class="stat-figure" style="color:var(--olive)">47%</span><span class="stat-text">is hard plastics, sheets and film, making up the majority of the microplastics mass.</span></li>
    <li class="stat"><span class="stat-figure" style="color:var(--crimson)">.05%</span><span class="stat-text">is foamed plastics – including polystyrene – making it a <span class="minor">minor</span> component of the GPGP.</span></li>
  </ul>
</div>
</body>
</html>
```